gift and delivery packeging of tulips and kites

we need a creative unique trendy design of packaging items including boxes , gift wrap , tissue paper, ribbons , tags , mailing bags ..inclusive cards.

our business is a medical concept boutique selling medical uniforms and medical accessories and gift to health care workers .
www.tulipsandkites.ae

```html
<!DOCTYPE html>
<html lang="en">
<head>
<meta charset="utf-8">
<title>Tulips and Kites – Lab-Coat Box</title>
<link rel="stylesheet" href="https://fonts.googleapis.com/css2?family=Montserrat:wght@700;800&family=Open+Sans:wght@400;600&display=swap">
<style>
  :root {
    --stage: #334247;
    --navy: #0f2a78;
    --royal: #1f4fd6;
    --sky: #46c9ec;
    --ice: #e3f6fc;
    --teal: #1b9cc9;
    --teal-dark: #157fa6;
    --white: #ffffff;
    --leaf: #3f9a3a;
  }
  * { margin: 0; padding: 0; box-sizing: border-box; }
  html, body { width: 1200px; height: 840px; overflow: hidden; }
  body {
    background: var(--stage);
    display: flex; flex-direction: column; align-items: center; justify-content: center;
    font-family: "Open Sans", Arial, sans-serif;
  }
  .box-lid {
    position: relative;
    width: 980px; height: 540px;
    background: linear-gradient(200deg, var(--ice) 0%, var(--sky) 45%, var(--royal) 100%);
    overflow: hidden;
  }
  .headline {
    position: absolute; left: 60px; top: 50px;
    font-family: "Montserrat", Arial, sans-serif; font-weight: 800;
    font-size: 44px; line-height: 1.05; letter-spacing: 1.5px;
    color: var(--navy); text-transform: uppercase;
  }
  .features {
    position: absolute; left: 64px; top: 172px;
    list-style: none; color: var(--navy);
    font-size: 19px; line-height: 1.4;
  }
  .features li::before { content: "•"; margin-right: 8px; }
  .brand {
    position: absolute; right: 48px; top: 48px;
    display: flex; align-items: center; gap: 12px;
  }
  .brand-dot { width: 46px; height: 46px; border-radius: 50%; background: var(--navy); flex: none; }
  .brand-name {
    font-family: "Montserrat", Arial, sans-serif; font-weight: 700;
    font-size: 26px; color: var(--navy);
  }
  .photo-area {
    position: absolute; right: 90px; bottom: 0;
    width: 380px; height: 390px;
    background: linear-gradient(180deg, #f4f8fb 0%, #dfe9f2 60%, #b9cfe2 100%);
  }
  .box-side {
    width: 980px; height: 150px;
    background: linear-gradient(180deg, var(--teal) 0%, var(--teal-dark) 100%);
    display: flex; justify-content: space-between; align-items: center;
    padding: 0 50px;
    color: var(--ice);
  }
  .contact { font-size: 17px; line-height: 1.35; font-style: normal; }
  .side-title { display: flex; align-items: center; gap: 18px; }
  .side-title .brand-dot { width: 56px; height: 56px; background: var(--white); border: 6px solid var(--leaf); }
  .side-label {
    font-family: "Montserrat", Arial, sans-serif; font-weight: 700;
    font-size: 20px; letter-spacing: 2px; text-transform: uppercase; text-align: right;
    color: var(--white); line-height: 1.25;
  }
</style>
</head>
<body>
  <section class="box-lid">
    <h1 class="headline">Men &amp; Women<br>Lab-Coats</h1>
    <ul class="features">
      <li>Flattering fit</li>
      <li>Wrinkle resistant</li>
      <li>Airlune fabric technology</li>
    </ul>
    <div class="brand">
      <span class="brand-dot"></span>
      <span class="brand-name">tulips and kites</span>
    </div>
    <div class="photo-area" role="img" aria-label="Photo of a man and a woman wearing white lab coats"></div>
  </section>
  <section class="box-side">
    <address class="contact">
      PO Box 41250 Corniche Road<br>
      Abu Dhabi, UAE<br>
      (+971) 2555 0142<br>
      info@tulipsandkites.ae
    </address>
    <div class="side-title">
      <span class="brand-dot"></span>
      <p class="side-label">Men &amp;<br>Women Lab-Coats</p>
    </div>
  </section>
</body>
</html>
```